Electrical company business card design.

Hi, were an electrical company in Auckland New Zealand called Quenra Ltd. We focus mainly on high end residential and commercial so the card would be targeted towards that.
The card will be for myself, i am the director of the company.
Name: Derek Polworth
Position: Director/electrician
Phone: 021 387 9142
Email: derek@quenra-example.co.nz
Location: Auckland
As for colors the the blue color in the logo is preferred, i also don't mind a black background option.
Target Market(s)
High end residential and commercial
Industry/Entity Type
Electrician
Contact Information for Business Card
Name: Derek Polworth Position: Director/Electrician Phone: 021 387 9142, Email: derek@quenra-example.co.nz, Location: Auckland

```html
<!DOCTYPE html>
<html lang="en">
<head>
<meta charset="utf-8">
<title>Quenra Ltd – Business Card</title>
<link href="https://fonts.googleapis.com/css2?family=Arimo:wght@400;700&display=swap" rel="stylesheet">
<style>
  :root {
    --backdrop: #3f3f3f;
    --blue-deep: #1547a0;
    --blue-bright: #0a8ad4;
    --card-white: #ffffff;
    --ink-grey: #4a4f55;
    --accent-blue: #1570c8;
    --text-light: #ffffff;
  }
  * { margin: 0; padding: 0; box-sizing: border-box; }
  html, body {
    width: 1200px;
    height: 803px;
    overflow: hidden;
    background: var(--backdrop);
    font-family: "Arimo", Arial, sans-serif;
  }
  .card-set {
    position: relative;
    width: 1200px;
    height: 803px;
    display: flex;
    align-items: center;
    justify-content: center;
    gap: 54px;
  }
  .card {
    width: 520px;
    height: 297px;
    border-radius: 22px;
    position: relative;
    overflow: hidden;
    box-shadow: 0 12px 28px rgba(0, 0, 0, 0.35);
  }
  .card-back {
    background: radial-gradient(ellipse at center, var(--blue-bright) 0%, var(--blue-deep) 75%);
    color: var(--text-light);
    display: flex;
    align-items: center;
    justify-content: center;
    gap: 16px;
  }
  .identity { text-align: right; }
  .person-name {
    font-weight: 700;
    font-size: 22px;
    letter-spacing: 0.2px;
  }
  .person-role {
    font-size: 12.5px;
    margin-top: 3px;
  }
  .divider {
    width: 1px;
    height: 44px;
    background: rgba(255, 255, 255, 0.6);
  }
  .contact { font-size: 13px; line-height: 1.6; }
  .contact-phone { display: flex; align-items: center; gap: 5px; }
  .contact-phone svg { width: 11px; height: 11px; fill: var(--text-light); }
  .card-front {
    background: var(--card-white);
    display: flex;
    align-items: center;
    justify-content: center;
  }
  .brand { display: flex; flex-direction: column; align-items: flex-start; }
  .brand-row { display: flex; align-items: center; gap: 14px; }
  .brand-mark {
    width: 34px;
    height: 34px;
    background: var(--accent-blue);
  }
  .brand-name {
    font-weight: 700;
    font-size: 54px;
    letter-spacing: 4px;
    color: var(--ink-grey);
    line-height: 1;
  }
  .brand-tagline {
    font-weight: 700;
    font-size: 13px;
    letter-spacing: 2.4px;
    color: var(--ink-grey);
    margin-top: 8px;
    margin-left: 48px;
  }
</style>
</head>
<body>
  <main class="card-set">
    <section class="card card-back">
      <div class="identity">
        <div class="person-name">Derek Polworth</div>
        <div class="person-role">Director/electrician</div>
      </div>
      <div class="divider"></div>
      <div class="contact">
        <div class="contact-location">Auckland</div>
        <div class="contact-phone">
          <svg viewBox="0 0 24 24" aria-hidden="true"><path d="M6.6 10.8c1.4 2.8 3.8 5.1 6.6 6.6l2.2-2.2c.3-.3.7-.4 1-.2 1.1.4 2.3.6 3.6.6.6 0 1 .4 1 1V20c0 .6-.4 1-1 1C10.6 21 3 13.4 3 4c0-.6.4-1 1-1h3.5c.6 0 1 .4 1 1 0 1.3.2 2.5.6 3.6.1.3 0 .7-.2 1z"/></svg>
          <span>021 387 9142</span>
        </div>
      </div>
    </section>
    <section class="card card-front">
      <div class="brand">
        <div class="brand-row">
          <span class="brand-mark"></span>
          <span class="brand-name">QUENRA</span>
        </div>
        <div class="brand-tagline">CRAFTED ELECTRICAL WORK</div>
      </div>
    </section>
  </main>
</body>
</html>
```